Corrabeen Holiday Village Flyer Project

Flyer required for a holiday caravan park. I have attached the current flyer for the park and would like to use the same layout. Please also alter the changes to the text that I have marked up. Until the additional uploads for the new images are ready, could you please just leave those as a blank square and the images can be inserted once I have them loaded.

Target Market(s)

Holiday makers

Industry/Entity Type

Tourism

Colors
3176b5
33a6d7
0393ce
fbee3e
fbed22
ffffff
faa54b

Requirements
Must have
• copy the attached flyer
• Would like a better title font for the front text - "Corrabeen Holiday Village", please make that a more playful holiday feel font
• Please use images 001 & 002 as the front cover images
• I have more images to load up which will be done 4/7.
Nice to have
• would like a better colour back ground to the flyer, maybe blue-ish and then alter the colour of the text accordingly
Should not have
• Please use the attached flyer copy as a template

```html
<!DOCTYPE html>
<html lang="en">
<head>
<meta charset="utf-8">
<title>Corrabeen Holiday Village – Trifold Flyer</title>
<link href="https://fonts.googleapis.com/css2?family=Fredoka:wght@600&family=Lato:wght@400;700;900&family=Tinos:wght@400;700&display=swap" rel="stylesheet">
<style>
:root{
  --blue:#3176b5;
  --blue-light:#3b88cc;
  --blue-deep:#2a66a6;
  --yellow:#fbee3e;
  --gold:#fcc419;
  --navy:#171a2b;
  --brown:#5a2a16;
  --white:#ffffff;
  --ink:#1f2230;
  --page:#e8ebee;
  --slot:#d5dde5;
  --slot-light:#e4e9ee;
  --serif:"Tinos", "Times New Roman", serif;
  --sans:"Lato", Arial, sans-serif;
  --fun:"Fredoka", "Lato", sans-serif;
}
*{box-sizing:border-box;margin:0;padding:0}
html,body{width:902px;height:1200px;overflow:hidden;background:var(--page)}
.sheet{position:absolute;display:flex;box-shadow:0 4px 14px rgba(0,0,0,.25)}
.sheet--outside{left:53px;top:61px;width:715px;height:510px}
.sheet--inside{left:136px;top:608px;width:715px;height:508px}
.panel{position:relative;height:100%;overflow:hidden}
.panel > svg.bg{position:absolute;left:0;top:0;width:100%;height:100%}
.abs{position:absolute}
.image-slot{position:absolute;background:var(--slot)}
.image-slot--framed{border:3px solid var(--white)}

/* outside: left panel */
.map{left:37px;top:22px;width:178px;height:182px;border:2px solid var(--white);background:var(--slot-light)}
.intro{left:26px;top:230px;width:192px;font:400 8.8px/11.6px var(--sans);color:var(--white);text-align:justify}
.activities{left:15px;top:301px;width:212px;height:82px;border:1.5px solid var(--yellow);border-radius:4px;padding:4px 8px;display:grid;grid-template-columns:118px 1fr;column-gap:8px;font:700 7px/1.15 var(--sans);color:var(--white)}
.activities ul{list-style:none;display:flex;flex-direction:column;justify-content:space-between}
.activities li.lead{white-space:nowrap;overflow:hidden}
.attractions{right:16px;top:432px;text-align:right;font-family:var(--serif);font-weight:700;line-height:1.1}
.attractions .a1{font-size:12.5px;color:var(--navy)}
.attractions .a2{font-size:12.5px;color:var(--blue)}
.attractions .a3{font-size:18px;color:var(--white)}

/* name setting */
.brand-name{font:600 19px/1.05 var(--fun);text-align:center;letter-spacing:.3px}
.contact{text-align:center;font-family:var(--serif)}

/* outside: middle panel */
.mid-brand{left:0;width:100%;top:238px;color:var(--white)}
.mid-contact{left:0;width:100%;top:306px;color:var(--white)}
.mid-contact .phone{font:700 11.5px var(--serif);margin-bottom:8px}
.mid-contact p{font-size:7.6px;line-height:14px}

/* outside: cover panel */
.cover-brand{left:0;width:100%;top:34px;color:var(--ink);font-size:22px}
.cover-contact{left:0;width:100%;top:424px;color:var(--navy)}
.cover-contact .phone{font:700 14px var(--serif);margin-bottom:3px}
.cover-contact p{font-size:8px;line-height:12px}
.cover-contact .web{font:700 11.5px var(--serif);margin-top:2px}

/* inside */
.heading{left:0;width:100%;text-align:center;font:400 17px var(--serif);letter-spacing:.5px}
.heading--light{color:var(--white)}
.heading--dark{color:var(--ink);font-weight:700}
.pill{left:24px;width:200px;height:16px;border-radius:5px;background:var(--yellow);color:var(--ink);font:700 7.4px/16px var(--sans);text-align:center}
.list{list-style:none;font:400 8px/17px var(--serif);color:var(--white);text-transform:uppercase}
.list--two{display:grid;grid-template-columns:104px 1fr}
.list--accom{color:var(--blue-deep);font-weight:700}
.list--near{font-size:7.4px;line-height:16px}
.info-band{right:6px;top:20px;width:50px;height:290px;writing-mode:vertical-rl;color:var(--navy);font-family:var(--serif)}
.info-band .note{font-size:8px;line-height:14px}
.info-band .line{font:700 11px var(--serif);line-height:22px;white-space:nowrap}
</style>
</head>
<body>

<section class="sheet sheet--outside">

  <div class="panel" style="width:242px;background:var(--blue)">
    <svg class="bg" viewBox="0 0 242 510" preserveAspectRatio="none">
      <path d="M0 420 C60 390 160 388 242 396 L242 510 L0 510Z" fill="var(--white)"/>
      <path d="M0 432 C70 408 160 406 242 412 L242 510 L0 510Z" fill="var(--gold)"/>
      <rect x="0" y="489" width="242" height="21" fill="var(--navy)"/>
    </svg>
    <div class="abs map" role="img" aria-label="Space for a street map showing the park location"></div>
    <p class="abs intro">We are the second turn to the left, after the bridge. Ideally located nestled between Kestrel Beach and the Estuary, 3mins south of the Corrabeen cut with all the the associated water activities and 15mins from Westhaven CBD boasting. A cage of activities such as:</p>
    <div class="abs activities">
      <ul>
        <li class="lead">Summer Concerts ..............................</li>
        <li class="lead">Festivals ..............................................</li>
        <li class="lead">Dolphin Tours.....................................</li>
        <li class="lead">Movie theatres...................................</li>
        <li class="lead">Superb Restaurants...........................</li>
      </ul>
      <ul>
        <li>Foreshore Markets</li>
        <li>Westhaven Arts Centre</li>
        <li>Wildlife parks</li>
        <li>Taverns</li>
        <li>Night Clubs</li>
      </ul>
    </div>
    <div class="abs attractions">
      <div class="a1">HISTORICAL SITES AND</div>
      <div class="a2">MANY MORE TOURIST</div>
      <div class="a3">ATTRACTIONS!</div>
    </div>
  </div>

  <div class="panel" style="width:236px;background:linear-gradient(180deg,var(--blue-light),var(--blue-deep))">
    <svg class="bg" viewBox="0 0 236 510" preserveAspectRatio="none">
      <path d="M0 112 C80 126 160 118 236 104 L236 118 C160 134 80 140 0 132Z" fill="var(--brown)"/>
      <defs><linearGradient id="strip" x1="0" y1="0" x2="1" y2="0"><stop offset="0" stop-color="#d7d9dc"/><stop offset=".5" stop-color="#fff"/><stop offset="1" stop-color="#d7d9dc"/></linearGradient></defs>
      <rect x="0" y="488" width="236" height="22" fill="url(#strip)"/>
    </svg>
    <div class="image-slot" style="left:0;top:0;width:236px;height:112px;clip-path:polygon(0 0,100% 0,100% 93%,66% 100%,33% 100%,0 98%)" role="img" aria-label="Space for a photo of the park swimming pool"></div>
    <div class="abs brand-name mid-brand">Corrabeen<br>Holiday Village</div>
    <div class="abs contact mid-contact">
      <div class="phone">Ph:08 9555 0142</div>
      <p>27 Shoreline Drive, Corrabeen 6200 WA</p>
      <p>Email: info@corrabeenholiday.com.au</p>
      <p>www.corrabeenholiday.com.au</p>
    </div>
  </div>

  <div class="panel" style="width:237px;background:var(--navy)">
    <svg class="bg" viewBox="0 0 237 510" preserveAspectRatio="none">
      <path d="M0 0 H237 V80 C160 100 80 118 0 124Z" fill="var(--white)"/>
      <path d="M0 124 C80 118 160 100 237 80 L237 96 C160 116 80 130 0 134Z" fill="var(--brown)"/>
      <path d="M0 392 C80 376 170 380 237 388 L237 410 L0 410Z" fill="var(--blue)"/>
      <path d="M0 404 C80 392 170 394 237 400 L237 488 L0 488Z" fill="var(--gold)"/>
    </svg>
    <div class="abs brand-name cover-brand">Corrabeen<br>Holiday Village</div>
    <div class="image-slot image-slot--framed" style="left:12px;top:126px;width:208px;height:146px;transform:rotate(-2deg)" role="img" aria-label="Space for cover image 001"></div>
    <div class="image-slot image-slot--framed" style="left:30px;top:274px;width:168px;height:116px;transform:rotate(1.5deg)" role="img" aria-label="Space for cover image 002"></div>
    <div class="abs contact cover-contact">
      <div class="phone">Ph:08 9555 0142</div>
      <p>27 Shoreline Drive, Corrabeen 6200 WA</p>
      <p>Email: info@corrabeenholiday.com.au</p>
      <div class="web">www.corrabeenholiday.com.au</div>
    </div>
  </div>
</section>

<section class="sheet sheet--inside">

  <div class="panel" style="width:242px;background:var(--blue)">
    <svg class="bg" viewBox="0 0 242 508" preserveAspectRatio="none">
      <path d="M0 306 C80 296 170 304 242 322 L242 508 L0 508Z" fill="var(--yellow)"/>
    </svg>
    <h2 class="abs heading heading--light" style="top:22px">WHAT TO DO?</h2>
    <div class="abs pill" style="top:58px">THE ESTUARY IS ONLY 2MINS TO THE EAST FOR</div>
    <ul class="abs list list--two" style="left:38px;top:80px">
      <li>Water Sports</li><li>Prawning</li>
      <li>Swimming</li><li>Boating</li>
      <li>Crabbing</li><li>Boat Ramp Access</li>
    </ul>
    <div class="abs pill" style="top:141px">THE ESTUARY IS ONLY 2MINS TO THE EAST FOR</div>
    <ul class="abs list list--two" style="left:33px;top:163px">
      <li>Water Skiing</li><li>Crabbing</li>
      <li>Sailing</li><li>Surfing</li>
      <li>Swimming</li><li>Boat Ramp Access</li>
      <li>Fishing</li><li>Beach Walking</li>
    </ul>
    <div class="abs pill" style="top:250px">SPORTING FACILITIES 5MINS</div>
    <ul class="abs list list--two" style="left:33px;top:276px">
      <li>Golfing</li><li>Bowls</li>
    </ul>
    <div class="image-slot" style="left:0;top:322px;width:242px;height:186px" role="img" aria-label="Space for a photo of a family crabbing from a jetty"></div>
  </div>

  <div class="panel" style="width:238px;background:linear-gradient(90deg,#e4e5e7,#ffffff 30%,#ffffff 70%,#e4e5e7)">
    <div class="image-slot" style="left:6px;top:20px;width:226px;height:155px" role="img" aria-label="Space for a sunset beach photo"></div>
    <h2 class="abs heading heading--dark" style="top:200px">ACCOMMODATION</h2>
    <ul class="abs list list--accom" style="left:48px;top:236px">
      <li>Chalets Ensuite &amp; Air Con</li>
      <li>Caravans</li>
      <li>Caravans &amp; Air Con</li>
      <li>Caravans Ensuite &amp; Air Con</li>
      <li>Powered Sites</li>
    </ul>
    <div class="image-slot" style="left:6px;top:330px;width:226px;height:132px" role="img" aria-label="Space for a dolphin photo"></div>
  </div>

  <div class="panel" style="width:235px;background:var(--blue)">
    <svg class="bg" viewBox="0 0 235 508" preserveAspectRatio="none">
      <path d="M235 0 H160 C150 80 175 120 150 200 C140 250 150 290 160 318 H235Z" fill="var(--yellow)"/>
      <path d="M0 350 C70 324 160 318 235 322 L235 340 C160 336 70 340 0 362Z" fill="var(--white)"/>
      <path d="M0 340 C70 318 160 312 235 316 L235 330 C160 326 70 330 0 352Z" fill="var(--yellow)"/>
    </svg>
    <div class="abs info-band">
      <div class="note">For more information please contact us or visit our website</div>
      <div class="line">Ph:08 9555 0142 &nbsp; www.corrabeenholiday.com.au</div>
    </div>
    <h2 class="abs heading heading--light" style="top:22px;width:140px">FACILITIES</h2>
    <ul class="abs list" style="left:38px;top:64px">
      <li>Eftpos</li><li>Swimming Pool</li><li>Undercover BBQ</li><li>Crab Cooker</li>
      <li>Playground</li><li>Laundrette</li><li>TV Room</li><li>Games Room</li>
    </ul>
    <ul class="abs list list--near" style="left:10px;top:228px">
      <li>2 Supermarkets within 2mins</li>
      <li>13 Take-away shops within 7mins</li>
      <li>6 Restaurants within 7mins</li>
      <li>Westhaven CBD 15mins</li>
    </ul>
    <div class="image-slot" style="left:0;top:340px;width:235px;height:168px;clip-path:polygon(0 12%,30% 4%,65% 0,100% 1%,100% 100%,0 100%)" role="img" aria-label="Space for an aerial photo of the estuary and bridge"></div>
  </div>
</section>

</body>
</html>
```